Powerpoint presentation sales pack for ground transfer company

Need a base pack for sales presentation for KLV,
We specialise in corporate ground transport (similar to ZOLTA)
Needs to be sharp and have a modern feel
Looking for a good master slide design and page layout for provide content
Check out our website https://klv.journeys/
Check out our competitors https://www.zolta.com/business https://www.marwickcarservice.com.au
Look at other marketing material available and old draft powerpoint pack for content and design ideas

```html
<!DOCTYPE html>
<html lang="en">
<head>
<meta charset="utf-8">
<title>KLV – Sales Presentation Pack</title>
<link href="https://fonts.googleapis.com/css2?family=Ubuntu:wght@300;400;500;700&display=swap" rel="stylesheet">
<style>
:root{
  --teal:#2db59f;
  --teal-dark:#23957f;
  --ink:#333333;
  --ink-soft:#666666;
  --mute:#9a9a9a;
  --paper:#ffffff;
  --mist:#f4f4f4;
  --night:#2c2f33;
  --band:#4a4a4a;
}
*{box-sizing:border-box;margin:0;padding:0}
html,body{width:1200px;height:1200px;overflow:hidden;background:var(--band)}
body{font-family:"Ubuntu",sans-serif;color:var(--ink)}
.stage{position:relative;width:1500px;height:1500px;transform:scale(.8);transform-origin:0 0;background:var(--band)}
.slide{position:absolute;overflow:hidden;background:var(--paper)}
.abs{position:absolute}
.photo{position:absolute}
.photo.warm{background:linear-gradient(135deg,#6b4b33,#c7955d 55%,#3b2c22)}
.photo.cool{background:linear-gradient(135deg,#1f2a38,#5f7894 55%,#b9c7d4)}
.photo.grey{background:linear-gradient(135deg,#3a3d42,#8c9096 60%,#cfd2d5)}
.photo.dusk{background:linear-gradient(180deg,#2a3342 0%,#8a6a5a 45%,#e09a48 62%,#3a2e2a 100%)}
.photo.light{background:linear-gradient(120deg,#e8eaec,#bfc4c8 60%,#f4f5f6)}
.photo.dark{background:linear-gradient(135deg,#1d1f22,#44484d 60%,#26282b)}
.photo.skin{background:linear-gradient(135deg,#8a6a52,#d2ad8d 50%,#5b4739)}
.photo.red{background:linear-gradient(135deg,#7a1d1a,#d24a35 50%,#3b2b2a)}
.t-teal{color:var(--teal)}
.h-slide{font-size:12px;font-weight:500;text-align:center;position:absolute;left:0;right:0}
.sub{font-size:4px;color:var(--mute);text-align:center;position:absolute;left:0;right:0}
.tiny{font-size:4.5px;line-height:1.4;color:var(--ink-soft)}
.small{font-size:6px;line-height:1.35}
.footer{position:absolute;left:0;right:0;bottom:0;height:8px;border-top:1.5px solid var(--teal);font-size:4px;color:var(--ink-soft);display:flex;justify-content:space-between;padding:1px 5px;background:var(--paper)}
.card{position:absolute;background:var(--paper);text-align:center}
.ico{width:26px;height:26px;stroke:var(--ink);fill:none;stroke-width:1.4}
.ico .tl{stroke:var(--teal)}
.ico .tf{fill:var(--teal);stroke:none}
.btn{display:inline-block;background:var(--teal);color:#fff;font-size:4px;padding:2px 7px;border-radius:1px}
.btn.round{border-radius:6px;background:var(--ink)}
.pill-label{position:absolute;left:0;right:0;bottom:0;height:12px;background:var(--teal);color:#fff;font-size:4.5px;display:flex;align-items:center;justify-content:center;font-weight:500}
.diamond{position:absolute;transform:rotate(45deg);border:2px solid #fff}
</style>
</head>
<body>
<div class="stage">

<!-- ========== ROW 1 ========== -->
<section class="slide" style="left:0;top:0;width:375px;height:210px">
  <div class="abs" style="left:22px;top:78px;font-size:13px;font-weight:300">KLV</div>
  <div class="abs t-teal" style="left:22px;top:92px;font-size:15px;font-weight:500">Ride Ready</div>
  <div class="abs tiny" style="left:22px;top:111px">The Calm Way to Arrive</div>
  <div class="abs tiny" style="left:22px;top:122px;font-size:4px">WWW.KLV.JOURNEYS</div>
  <div class="photo warm diamond" role="img" aria-label="Car photograph" style="left:170px;top:-60px;width:140px;height:140px"></div>
  <div class="photo cool diamond" role="img" aria-label="Car front detail photograph" style="left:200px;top:40px;width:120px;height:120px"></div>
  <div class="photo dusk diamond" role="img" aria-label="Car side photograph" style="left:130px;top:110px;width:120px;height:120px"></div>
  <div class="photo grey diamond" role="img" aria-label="Parked cars photograph" style="left:290px;top:130px;width:110px;height:110px"></div>
  <div class="photo light diamond" role="img" aria-label="Car interior photograph" style="left:320px;top:20px;width:90px;height:90px"></div>
</section>

<section class="slide" style="left:375px;top:0;width:375px;height:210px;background:#2a2d31">
  <div class="photo dark" role="img" aria-label="Dark car front photograph" style="inset:0;opacity:.9"></div>
  <div class="abs" style="left:17px;top:0;width:73px;height:195px;background:var(--teal);clip-path:polygon(0 0,100% 0,100% 88%,0 100%)"></div>
  <div class="abs" style="left:24px;top:56px;font-size:3.5px;color:#e6fffa">Table of Content</div>
  <div class="abs" style="left:24px;top:62px;font-size:13px;color:#fff;font-weight:500">AGENDA</div>
  <div class="abs" style="left:24px;top:81px;width:62px;font-size:3.5px;color:#e6fffa;line-height:1.4">Lorem ipsum dolor sit amet, consectetur adipiscing elit, sed do eiusmod tempor incididunt ut labore et dolore magna</div>
  <div class="abs" style="left:106px;top:56px;width:240px;display:grid;grid-template-columns:repeat(3,1fr);row-gap:28px;column-gap:10px;color:#fff">
    <div><div style="font-size:8px">2:45<span style="font-size:3px">PM</span></div><div style="font-size:4.5px;font-weight:500;margin:2px 0">WELCOME MESSAGE</div><div style="font-size:3.5px;color:#bbb;line-height:1.4">Lorem ipsum dolor sit amet, consectetur adipiscing elit, sed do eiusmod tempor</div></div>
    <div><div style="font-size:8px">5:20<span style="font-size:3px">PM</span></div><div style="font-size:4.5px;font-weight:500;margin:2px 0">ABOUT COMPANY</div><div style="font-size:3.5px;color:#bbb;line-height:1.4">Lorem ipsum dolor sit amet, consectetur adipiscing elit, sed do eiusmod tempor</div></div>
    <div><div style="font-size:8px">3:00<span style="font-size:3px">PM</span></div><div style="font-size:4.5px;font-weight:500;margin:2px 0">INTRODUCTION</div><div style="font-size:3.5px;color:#bbb;line-height:1.4">Lorem ipsum dolor sit amet, consectetur adipiscing elit, sed do eiusmod tempor</div></div>
    <div><div style="font-size:8px">17:35</div><div style="font-size:4.5px;font-weight:500;margin:2px 0">OUR PORTFOLIO</div><div style="font-size:3.5px;color:#bbb;line-height:1.4">Lorem ipsum dolor sit amet, consectetur adipiscing elit, sed do eiusmod tempor</div></div>
    <div><div style="font-size:8px">12:10</div><div style="font-size:4.5px;font-weight:500;margin:2px 0">OUR SPONSORS</div><div style="font-size:3.5px;color:#bbb;line-height:1.4">Lorem ipsum dolor sit amet, consectetur adipiscing elit, sed do eiusmod tempor</div></div>
    <div><div style="font-size:8px">2:00<span style="font-size:3px">PM</span></div><div style="font-size:4.5px;font-weight:500;margin:2px 0">QUESTIONS</div><div style="font-size:3.5px;color:#bbb;line-height:1.4">Lorem ipsum dolor sit amet, consectetur adipiscing elit, sed do eiusmod tempor</div></div>
  </div>
</section>

<section class="slide" style="left:750px;top:0;width:375px;height:210px">
  <div class="abs" style="left:34px;top:48px;font-size:17px;font-weight:500">WELCOME</div>
  <div class="abs" style="left:34px;top:71px;font-size:7px">MESSAGE</div>
  <div class="abs tiny" style="left:34px;top:93px;width:100px">Lorem ipsum dolor sit amet, consectetur adipiscing elit, sed do eiusmod tempor incididunt ut labore et dolore magna aliqua.<br><br>Duis aute irure dolor in reprehenderit in voluptate velit esse cillum dolore eu fugiat nulla pariatur. Excepteur sint occaecat cupidatat non proident, sunt in culpa qui officia deserunt mollit</div>
  <div class="photo warm" role="img" aria-label="Chauffeur at the steering wheel photograph" style="left:188px;top:0;width:187px;height:210px;background:linear-gradient(135deg,#1e1c1b,#5a4636 50%,#b58a5a 80%,#2a2220)"></div>
  <svg class="abs" style="left:265px;top:88px" width="30" height="30" viewBox="0 0 30 30" fill="none" stroke="#fff" stroke-width="1.2"><circle cx="15" cy="15" r="13"/><circle cx="15" cy="15" r="3"/><path d="M3 13h9M18 13h9M15 18v9"/></svg>
</section>

<section class="slide" style="left:1125px;top:0;width:375px;height:210px">
  <div class="abs" style="left:16px;top:62px;font-size:15px;font-weight:500">About Us</div>
  <ul class="abs tiny" style="left:20px;top:90px;width:140px;list-style:disc;font-size:4.2px">
    <li>Privately held business established in 2011</li>
    <li>Innovators in technology</li>
    <li>Specialists in Corporate Transfers</li>
    <li>Extensive Network across all major cities in Australia<br>&nbsp;&nbsp;➢ Coverage in selected cities internationally</li>
    <li>Trusted by some of the largest TMCs in the country</li>
  </ul>
  <div class="photo light" role="img" aria-label="Passenger in car photograph" style="left:166px;top:0;width:80px;height:70px"></div>
  <div class="abs" style="left:246px;top:0;width:129px;height:70px;background:#3a3a3a;color:#fff;padding:15px 0 0 26px">
    <div style="font-size:11px;font-weight:500;line-height:1.1">The Calm<br>Way to Arrive</div>
    <div style="font-size:4px;margin-top:3px">Visit us at: KLV.JOURNEYS</div>
  </div>
  <div class="photo skin" role="img" aria-label="Business man writing photograph" style="left:166px;top:70px;width:209px;height:80px"></div>
  <div class="abs" style="left:166px;top:150px;width:65px;height:60px;background:var(--teal);color:#fff;padding:10px 0 0 10px">
    <div style="font-size:16px;font-weight:500">KLV</div><div style="font-size:3.5px">RIDE READY</div>
  </div>
  <div class="photo cool" role="img" aria-label="Passengers in back seat photograph" style="left:231px;top:150px;width:68px;height:60px"></div>
  <div class="photo grey" role="img" aria-label="Car on road photograph" style="left:299px;top:150px;width:76px;height:60px"></div>
</section>

<!-- ========== ROW 2 ========== -->
<section class="slide" style="left:0;top:210px;width:375px;height:210px">
  <div class="abs" style="left:33px;top:38px"><span style="font-size:4px;color:var(--mute)">Services of</span> <span style="font-size:14px;font-weight:500">KLV</span></div>
  <div class="card" style="left:33px;top:68px;width:95px;height:110px;background:var(--mist);text-align:left;padding:40px 8px 0">
    <div class="photo cool" role="img" aria-label="Airport portrait photograph" style="left:7px;top:-1px;width:28px;height:28px;border-radius:50%"></div>
    <div class="small" style="font-weight:500">Airport Transfers</div>
    <div class="tiny" style="font-size:3.6px;margin-top:3px">When it comes to flying, being late isn't an option. At KLV, you can count on us to be on time, guaranteed. We have a superior network of drivers.</div>
    <div class="tiny" style="font-size:3.6px;margin-top:4px;text-decoration:underline">Learn More</div>
  </div>
  <div class="card" style="left:136px;top:68px;width:95px;height:110px;background:var(--mist);text-align:left;padding:40px 8px 0">
    <div class="photo cool" role="img" aria-label="Business traveller photograph" style="left:7px;top:-1px;width:28px;height:28px;border-radius:50%"></div>
    <div class="small" style="font-weight:500">Corporate Roadshow</div>
    <div class="tiny" style="font-size:3.6px;margin-top:3px">We understand the specific needs of the business traveller. No matter where you are in the world, we will deliver a high quality, seamless experience, every time.</div>
    <div class="tiny" style="font-size:3.6px;margin-top:4px;text-decoration:underline">Learn More</div>
  </div>
  <div class="card" style="left:239px;top:68px;width:95px;height:110px;background:var(--mist);text-align:left;padding:40px 8px 0">
    <div class="photo light" role="img" aria-label="Event guests photograph" style="left:7px;top:-1px;width:28px;height:28px;border-radius:50%"></div>
    <div class="small" style="font-weight:500">Concerts &amp; Events</div>
    <div class="tiny" style="font-size:3.6px;margin-top:3px">We are experienced in providing dependable, high quality transport to and from concerts and events. We can cater for everything from small, private events.</div>
    <div class="tiny" style="font-size:3.6px;margin-top:4px;text-decoration:underline">Learn More</div>
  </div>
  <div class="footer"><span>Ride Ready</span><span>Page Number 5</span></div>
</section>

<section class="slide" style="left:375px;top:210px;width:375px;height:210px">
  <div class="abs" style="left:31px;top:48px;font-size:15px;font-weight:300">About</div>
  <div class="abs" style="left:31px;top:68px;font-size:18px;font-weight:700">OUR DRIVERS</div>
  <div class="abs" style="left:31px;top:92px;font-size:6.5px;color:var(--ink-soft)">KLV - The Calm Way to Arrive</div>
  <div class="abs" style="left:28px;top:136px;display:flex;gap:14px">
    <div style="display:flex;gap:5px;width:105px">
      <svg class="ico" viewBox="0 0 26 26"><circle cx="13" cy="13" r="11"/><circle class="tl" cx="13" cy="11" r="4"/><path d="M6 21c2-4 12-4 14 0"/></svg>
      <div><div style="font-size:5.5px;font-weight:500">Discreet and Professional</div><div class="tiny" style="font-size:3.8px;margin-top:3px">KLV partners with Industry Established, Authorised, and Insured Drivers</div></div>
    </div>
    <div style="display:flex;gap:5px;width:105px">
      <svg class="ico" viewBox="0 0 26 26"><path d="M8 4h10v3l-2 2v8l3 2v4H7v-4l3-2V9L8 7z"/><path class="tl" d="M10 12h6M10 15h6"/></svg>
      <div><div style="font-size:5.5px;font-weight:500">Extensive pre screening checks</div><div class="tiny" style="font-size:3.8px;margin-top:3px">Driver service commitment, <b>"Driven"</b> by Continuous Improvement.</div></div>
    </div>
    <div style="display:flex;gap:5px;width:105px">
      <svg class="ico" viewBox="0 0 26 26"><path d="M4 20l8-8 3 3 7-9"/><circle class="tl" cx="9" cy="8" r="3"/></svg>
      <div><div style="font-size:5.5px;font-weight:500">GPS tracking on on time performance monitoring</div></div>
    </div>
  </div>
</section>

<section class="slide" style="left:750px;top:210px;width:375px;height:210px">
  <div class="h-slide" style="top:15px;font-size:10px">Our Drivers</div>
  <div class="sub" style="top:31px">Your Subtitle Goes Here</div>
  <div class="abs" style="left:38px;top:52px;width:300px;display:grid;grid-template-columns:repeat(3,1fr);row-gap:14px;text-align:center;font-size:6px;line-height:1.25">
    <div><svg class="ico" viewBox="0 0 26 26"><circle cx="13" cy="13" r="11"/><circle class="tl" cx="13" cy="11" r="4"/><path d="M6 21c2-4 12-4 14 0"/></svg><div style="margin-top:10px"><b style="font-weight:500">Discreet</b> and<br>Professional</div></div>
    <div><svg class="ico" viewBox="0 0 26 26"><path d="M8 4h10v3l-2 2v8l3 2v4H7v-4l3-2V9L8 7z"/><path class="tl" d="M10 12h6M10 15h6"/></svg><div style="margin-top:10px"><b style="font-weight:500">KLV</b> partners with Industry<br>Established, Authorised,<br>and Insured Drivers</div></div>
    <div><svg class="ico" viewBox="0 0 26 26"><rect x="6" y="3" width="14" height="20"/><path class="tl" d="M9 8h8M9 12h8M9 16h8"/></svg><div style="margin-top:10px"><b style="font-weight:500">Extensive</b> pre<br>screening checks</div></div>
    <div><svg class="ico" viewBox="0 0 26 26"><circle cx="13" cy="13" r="11"/><circle class="tl" cx="13" cy="13" r="6"/><path d="M10 13l2 2 4-4"/></svg><div style="margin-top:8px"><b style="font-weight:500">Driver</b> service<br>commitment</div></div>
    <div><svg class="ico" viewBox="0 0 26 26"><rect x="6" y="3" width="14" height="20"/><path class="tl" d="M9 17l3-4 3 2 3-6"/></svg><div style="margin-top:8px"><b style="font-weight:500">"Driven"</b> by Continuous<br>Improvement</div></div>
    <div><svg class="ico" viewBox="0 0 26 26"><path d="M4 20l8-8 3 3 7-9"/><circle class="tl" cx="9" cy="8" r="3"/></svg><div style="margin-top:8px"><b style="font-weight:500">GPS tracking</b> on on<br>time performance<br>monitoring</div></div>
  </div>
</section>

<section class="slide" style="left:1125px;top:210px;width:375px;height:210px">
  <div class="abs" style="left:40px;top:120px;font-size:4px;color:var(--mute)">KLV Offers</div>
  <div class="abs" style="left:40px;top:127px;font-size:20px;font-weight:500">CALM</div>
  <div class="abs" style="left:40px;top:153px;font-size:8px;color:var(--ink-soft);font-weight:300">Way to Arrive</div>
  <div class="photo grey" role="img" aria-label="Man with laptop photograph" style="left:60px;top:48px;width:67px;height:53px"></div>
  <div class="photo cool" role="img" aria-label="Smiling driver photograph" style="left:131px;top:20px;width:155px;height:81px"></div>
  <div class="photo skin" role="img" aria-label="Couple in car photograph" style="left:131px;top:105px;width:98px;height:85px"></div>
  <div class="photo cool" role="img" aria-label="Sedan photograph" style="left:233px;top:105px;width:53px;height:46px"></div>
  <div class="abs" style="left:235px;top:157px;font-size:6px;font-weight:500">The KLV Difference</div>
  <div class="abs tiny" style="left:235px;top:167px;width:110px;font-size:3.8px">Lorem ipsum dolor sit amet, consectetur adipiscing elit, sed do eiusmod tempor</div>
</section>

<!-- ========== ROW 3 ========== -->
<section class="slide" style="left:0;top:420px;width:375px;height:210px;background:#2d2f31">
  <div class="photo dark" role="img" aria-label="Black and white building photograph" style="inset:0"></div>
  <div class="h-slide" style="top:15px;color:#fff;font-size:10px">Our Vehicles</div>
  <div class="sub" style="top:31px;color:#bbb">Your Subtitle Goes Here</div>
  <div class="card" style="left:53px;top:63px;width:84px;height:83px;padding-top:6px">
    <svg width="26" height="22" viewBox="0 0 26 22"><rect x="2" y="3" width="22" height="12" fill="#3bb54a"/><circle cx="13" cy="9" r="3" fill="#fff"/><circle cx="17" cy="15" r="4" fill="#f3b23a"/></svg>
    <div style="font-size:5px;font-weight:500;margin:5px 0">RANGING</div>
    <div class="tiny" style="font-size:3.8px;padding:0 4px">Late model vehicles ranging from Hartwell Coupe to Velmont &amp; European Vehicles</div>
  </div>
  <div class="card" style="left:145px;top:63px;width:84px;height:83px;padding-top:6px">
    <svg width="26" height="22" viewBox="0 0 26 22"><path d="M4 9l3-5h12l3 5v7H4z" fill="var(--teal)"/><rect x="8" y="5" width="10" height="4" fill="#dff"/><circle cx="8" cy="16" r="2" fill="#333"/><circle cx="18" cy="16" r="2" fill="#333"/></svg>
    <div style="font-size:5px;font-weight:500;margin:5px 0">VEHICLES</div>
    <div class="tiny" style="font-size:3.8px;padding:0 4px">Various vehicle types available - Sedans, People Movers and Buses</div>
  </div>
  <div class="card" style="left:236px;top:63px;width:84px;height:83px;padding-top:6px">
    <svg width="30" height="22" viewBox="0 0 30 22"><rect x="1" y="4" width="28" height="14" fill="#3a3a3a"/><rect x="3" y="6" width="11" height="10" fill="#3bb54a"/><rect x="16" y="6" width="11" height="10" fill="#3bb54a"/></svg>
    <div style="font-size:5px;font-weight:500;margin:5px 0">FEATURES</div>
    <div class="tiny" style="font-size:3.8px;padding:0 4px">Smart Drive option with complementary Wi-Fi and water</div>
  </div>
</section>

<section class="slide" style="left:375px;top:420px;width:750px;height:420px">
  <div class="photo dusk" role="img" aria-label="Car side at sunset photograph" style="left:240px;top:0;width:510px;height:208px"></div>
  <div class="photo dark" role="img" aria-label="Car wheel on asphalt photograph" style="left:240px;top:360px;width:510px;height:60px"></div>
  <div class="abs" style="left:93px;top:142px;font-size:20px;font-weight:300">OUR</div>
  <div class="abs" style="left:93px;top:166px;font-size:28px;font-weight:700">VEHICLES</div>
  <div class="abs" style="left:93px;top:208px;width:147px;height:153px;background:var(--teal);color:#fff;padding:12px">
    <div style="font-size:26px;font-weight:300;line-height:.8">+</div>
    <div style="position:absolute;left:12px;bottom:10px;font-size:8px;line-height:1.3">Lorem ipsum dolor sit<br>amet, consectetur</div>
  </div>
  <div class="abs" style="left:240px;top:208px;width:510px;height:152px;display:grid;grid-template-columns:repeat(3,1fr);text-align:center;padding-top:14px">
    <div><svg width="52" height="48" viewBox="0 0 52 48"><rect x="2" y="4" width="46" height="26" fill="#3bb54a"/><circle cx="25" cy="17" r="7" fill="#fff"/><circle cx="34" cy="34" r="10" fill="#f3b23a"/></svg>
      <div style="font-size:11px;font-weight:500;margin:9px 0 12px">RANGING</div>
      <div style="font-size:8px;color:var(--ink-soft);line-height:1.35">Late model vehicles ranging from<br>Hartwell Coupe to Velmont &amp;<br>European Vehicles</div></div>
    <div><svg width="56" height="48" viewBox="0 0 56 48"><path d="M6 22l6-14h32l6 14v14H6z" fill="var(--teal)"/><rect x="14" y="10" width="28" height="10" fill="#d9f6f0"/><circle cx="16" cy="36" r="5" fill="#333"/><circle cx="40" cy="36" r="5" fill="#333"/></svg>
      <div style="font-size:11px;font-weight:500;margin:9px 0 12px">VEHICLES</div>
      <div style="font-size:8px;color:var(--ink-soft);line-height:1.35">Various vehicle types<br>available - Sedans, People<br>Movers and Buses</div></div>
    <div><svg width="64" height="48" viewBox="0 0 64 48"><rect x="2" y="8" width="60" height="30" fill="#3a3a3a"/><rect x="6" y="12" width="25" height="22" fill="#3bb54a"/><rect x="34" y="12" width="25" height="22" fill="#3bb54a"/></svg>
      <div style="font-size:11px;font-weight:500;margin:9px 0 12px">FEATURES</div>
      <div style="font-size:8px;color:var(--ink-soft);line-height:1.35">Smart Drive option with<br>complementary Wi-Fi<br>and water</div></div>
  </div>
</section>

<section class="slide" style="left:1125px;top:420px;width:375px;height:210px">
  <div class="h-slide" style="top:15px;font-size:10px">KLV Service Offering</div>
  <div class="sub" style="top:31px">Your Subtitle Goes Here</div>
  <div class="abs" style="left:27px;top:63px;width:321px;height:113px;display:grid;grid-template-columns:repeat(4,1fr);gap:2px">
    <div class="photo grey" role="img" aria-label="Executive sedan photograph" style="position:relative"><div class="pill-label" style="top:48px;bottom:auto">EXECUTIVE &amp; BUSINESS</div></div>
    <div class="photo dark" role="img" aria-label="People mover photograph" style="position:relative"><div class="pill-label" style="top:48px;bottom:auto;background:var(--ink)">PEOPLE MOVER</div></div>
    <div class="photo dusk" role="img" aria-label="Premium car photograph" style="position:relative"><div class="pill-label" style="top:48px;bottom:auto">KLV PREMIUM</div></div>
    <div class="photo cool" role="img" aria-label="Standard sedan photograph" style="position:relative"><div class="pill-label" style="top:48px;bottom:auto;background:var(--ink)">KLV RIDE</div></div>
  </div>
  <div class="footer"><span>Ride Ready</span><span>Page Number 11</span></div>
</section>

<!-- ========== ROW 4 ========== -->
<section class="slide" style="left:0;top:630px;width:375px;height:210px">
  <div class="h-slide" style="top:14px;font-size:10px">KLV Service Offering</div>
  <div class="sub" style="top:30px">Your Subtitle Goes Here</div>
  <div class="abs" style="left:25px;top:53px;width:80px;font-size:5.5px;line-height:1.25">
    <div style="font-weight:500">Executive &amp;<br>Business Sedans</div>
    <div class="tiny" style="font-size:3.6px">• Airport Meet and Greet<br>• Services with signboard<br>• Luxury Sedans</div>
    <div style="font-weight:500;margin-top:8px">People Movers</div>
    <div class="tiny" style="font-size:3.6px">• Larger Luxury Velmont<br>Vans Vehicles</div>
    <div style="font-weight:500;margin-top:8px">KLV Premium</div>
    <div class="tiny" style="font-size:3.6px">• Luxury Sedans</div>
    <div style="font-weight:500;margin-top:8px">KLV Ride</div>
    <div class="tiny" style="font-size:3.6px">• Standard Private Sedans<br>• Cheaper Alternative</div>
  </div>
  <div class="abs" style="left:105px;top:48px;width:270px;height:128px;display:grid;grid-template-columns:repeat(4,1fr);gap:1px">
    <div class="photo cool" role="img" aria-label="Executive sedan photograph" style="position:relative"><div class="pill-label" style="background:var(--ink)">EXECUTIVE &amp; BUSINESS</div></div>
    <div class="photo cool" role="img" aria-label="People mover photograph" style="position:relative"><div class="pill-label">PEOPLE MOVERS</div></div>
    <div class="photo light" role="img" aria-label="Premium sedan photograph" style="position:relative"><div class="pill-label" style="background:var(--ink)">KLV PREMIUM</div></div>
    <div class="photo grey" role="img" aria-label="Parked sedan photograph" style="position:relative"><div class="pill-label">KLV RIDE</div></div>
  </div>
  <div class="footer"><span>Ride Ready</span><span>Page Number 12</span></div>
</section>

<section class="slide" style="left:1125px;top:630px;width:375px;height:210px;background:#e9eaeb">
  <div class="photo light" role="img" aria-label="Cloudy sky photograph" style="inset:0"></div>
  <div class="h-slide" style="top:15px;font-size:10px">Airport Transfers</div>
  <div class="sub" style="top:31px">Your Subtitle Goes Here</div>
  <svg class="abs" style="left:170px;top:42px" width="40" height="20" viewBox="0 0 40 20" fill="#555"><path d="M2 12l34-6c3 0 3 3 0 3L22 12l-8 7h-3l5-6-9 1-3 3H2l2-4z"/></svg>
  <div class="abs" style="left:27px;top:80px;width:321px;display:grid;grid-template-columns:repeat(4,1fr);text-align:center">
    <div><div style="width:32px;height:32px;border-radius:50%;background:#fff;margin:0 auto;display:flex;align-items:center;justify-content:center"><svg width="16" height="16" viewBox="0 0 16 16" fill="none" stroke="#333"><rect x="3" y="4" width="10" height="10"/><path d="M6 4V2h4v2" stroke="var(--teal)"/></svg></div><div style="font-size:6.5px;font-weight:500;margin:6px 0 3px">Travels</div><div class="tiny" style="font-size:3.6px;padding:0 4px">Lorem ipsum dolor sit amet, consectetur adipiscing elit, sed do eiusmod tempor incididunt ut</div></div>
    <div><div style="width:32px;height:32px;border-radius:50%;background:#fff;margin:0 auto;display:flex;align-items:center;justify-content:center"><svg width="18" height="14" viewBox="0 0 18 14"><rect x="1" y="2" width="16" height="10" fill="var(--teal)"/><circle cx="9" cy="7" r="3" fill="#fff"/></svg></div><div style="font-size:6.5px;font-weight:500;margin:6px 0 3px">Best Price</div><div class="tiny" style="font-size:3.6px;padding:0 4px">Lorem ipsum dolor sit amet, consectetur adipiscing elit, sed do eiusmod tempor incididunt ut</div></div>
    <div><div style="width:32px;height:32px;border-radius:50%;background:#fff;margin:0 auto;display:flex;align-items:center;justify-content:center"><svg width="16" height="16" viewBox="0 0 16 16" fill="none" stroke="#333"><rect x="3" y="2" width="10" height="12"/><path d="M5 10l2-3 2 2 2-4" stroke="var(--teal)"/></svg></div><div style="font-size:6.5px;font-weight:500;margin:6px 0 3px">Account Reports</div><div class="tiny" style="font-size:3.6px;padding:0 4px">Lorem ipsum dolor sit amet, consectetur adipiscing elit, sed do eiusmod tempor incididunt ut</div></div>
    <div><div style="width:32px;height:32px;border-radius:50%;background:#fff;margin:0 auto;display:flex;align-items:center;justify-content:center"><svg width="16" height="16" viewBox="0 0 16 16" fill="none" stroke="#333"><rect x="3" y="2" width="10" height="12"/><path d="M5 6h6M5 9h6" stroke="var(--teal)"/></svg></div><div style="font-size:6.5px;font-weight:500;margin:6px 0 3px">Free of Charge</div><div class="tiny" style="font-size:3.6px;padding:0 4px">Lorem ipsum dolor sit amet, consectetur adipiscing elit, sed do eiusmod tempor incididunt ut</div></div>
  </div>
  <div class="footer"><span>Ride Ready</span><span>Page Number 16</span></div>
</section>

<!-- ========== ROW 5 ========== -->
<section class="slide" style="left:0;top:840px;width:375px;height:210px">
  <div class="abs" style="left:0;top:0;width:375px;height:105px;display:grid;grid-template-columns:repeat(3,1fr);text-align:center">
    <div style="padding:12px 10px 0"><svg class="ico" viewBox="0 0 26 26"><path d="M4 8h18M8 4v8M14 14l6 6"/><circle class="tl" cx="18" cy="8" r="3"/></svg><div style="font-size:8px;font-weight:500;margin-top:4px">Quality</div><div class="tiny" style="font-size:3.6px">Lorem ipsum dolor sit amet</div><div class="tiny" style="font-size:3.6px;margin-top:3px">Lorem ipsum dolor sit amet, consectetur adipiscing elit, sed do eiusmod tempor incididunt ut labore et dolore magna aliqua.</div></div>
    <div style="padding:12px 10px 0;background:var(--teal);color:#fff"><svg width="26" height="26" viewBox="0 0 26 26" fill="none" stroke="#fff" stroke-width="1.4"><circle cx="13" cy="13" r="9"/><circle cx="13" cy="10" r="3"/><path d="M8 19c2-4 8-4 10 0"/></svg><div style="font-size:8px;font-weight:500;margin-top:4px">Powerful</div><div style="font-size:3.6px;line-height:1.4">Lorem ipsum dolor sit amet</div><div style="font-size:3.6px;line-height:1.4;margin-top:3px">Lorem ipsum dolor sit amet, consectetur adipiscing elit, sed do eiusmod tempor incididunt ut labore et dolore magna aliqua.</div></div>
    <div style="padding:12px 10px 0"><svg class="ico" viewBox="0 0 26 26"><rect x="5" y="6" width="16" height="14"/><rect class="tf" x="12" y="3" width="6" height="6"/></svg><div style="font-size:8px;font-weight:500;margin-top:4px">Versatile</div><div class="tiny" style="font-size:3.6px">Lorem ipsum dolor sit amet</div><div class="tiny" style="font-size:3.6px;margin-top:3px">Lorem ipsum dolor sit amet, consectetur adipiscing elit, sed do eiusmod tempor incididunt ut labore et dolore magna aliqua.</div></div>
  </div>
  <div class="photo skin" role="img" aria-label="Two children in car back seat photograph" style="left:0;top:105px;width:375px;height:105px"></div>
</section>

<section class="slide" style="left:375px;top:840px;width:375px;height:210px;background:#3b3d40">
  <div class="photo dark" role="img" aria-label="Dark car on road photograph" style="inset:0;background:linear-gradient(135deg,#2b2d30,#5d6166 55%,#3a3c3f)"></div>
  <div class="abs" style="left:52px;top:38px;font-size:3.5px;color:#ccc">Ride Ready</div>
  <div class="abs" style="left:52px;top:46px;font-size:9px;color:#fff;font-weight:500">Range of Services</div>
  <div class="abs" style="left:52px;top:61px;width:140px;font-size:4px;color:#ddd;line-height:1.35">We cater for a wide range of transport requirements – from airport transfers and meeting transport, to roadshows and large-scale corporate events. Our fleet includes everything from luxury sedans to people movers and we can even provide buses (on request).</div>
  <div class="abs" style="left:53px;top:133px;width:268px;display:grid;grid-template-columns:repeat(3,1fr);gap:5px">
    <div style="background:#fff;height:56px;padding:5px"><svg width="18" height="18" viewBox="0 0 18 18" fill="none" stroke="#333"><circle cx="9" cy="9" r="7"/><path d="M6 12V7l3-2 3 2v5" stroke="var(--teal)"/></svg><div style="font-size:5px;font-weight:500">Lorem Ipsum</div><div class="tiny" style="font-size:3.5px">Lorem ipsum dolor sit amet, consectetur adipiscing elit, sed do eiusmod tempor incididunt ut</div></div>
    <div style="background:#fff;height:56px;padding:5px"><svg width="18" height="18" viewBox="0 0 18 18"><circle cx="9" cy="9" r="7" fill="var(--teal)"/><circle cx="9" cy="7" r="2.5" fill="#fff"/></svg><div style="font-size:5px;font-weight:500">Lorem Ipsum</div><div class="tiny" style="font-size:3.5px">Lorem ipsum dolor sit amet, consectetur adipiscing elit, sed do eiusmod tempor incididunt ut</div></div>
    <div style="background:#fff;height:56px;padding:5px"><svg width="18" height="18" viewBox="0 0 18 18" fill="none" stroke="#333"><circle cx="9" cy="9" r="7"/><path d="M4 9h10M9 2c3 3 3 11 0 14" stroke="var(--teal)"/></svg><div style="font-size:5px;font-weight:500">Lorem Ipsum</div><div class="tiny" style="font-size:3.5px">Lorem ipsum dolor sit amet, consectetur adipiscing elit, sed do eiusmod tempor incididunt ut</div></div>
  </div>
</section>

<section class="slide" style="left:750px;top:840px;width:750px;height:420px;background:#f3f3f3">
  <div class="photo light" role="img" aria-label="Silver car front photograph" style="left:430px;top:0;width:320px;height:420px;background:radial-gradient(ellipse at 70% 55%,#b8bcc0,#e4e6e8 55%,#f3f3f3 75%)"></div>
  <div class="abs" style="left:65px;top:62px;font-size:32px;font-weight:700">RIDE READY</div>
  <div class="abs" style="left:65px;top:102px;font-size:22px;font-weight:300">The Differences</div>
  <div class="abs" style="left:68px;top:165px;width:360px;display:grid;grid-template-columns:repeat(3,1fr);row-gap:30px">
    <div><svg width="40" height="36" viewBox="0 0 40 36" fill="none" stroke="#333" stroke-width="1.4"><rect x="2" y="2" width="16" height="30"/><circle cx="26" cy="14" r="8" stroke="var(--teal)"/><circle cx="26" cy="14" r="3" fill="var(--teal)" stroke="none"/></svg><div style="font-size:15px;font-weight:500;margin-top:6px">Technology</div><div style="font-size:8.5px;color:var(--ink-soft)">Driven Business</div></div>
    <div><svg width="40" height="36" viewBox="0 0 40 36" fill="none" stroke="#333" stroke-width="1.4"><circle cx="20" cy="20" r="13"/><path d="M20 20l5-7M17 4h6" stroke="var(--teal)"/></svg><div style="font-size:15px;font-weight:500;margin-top:6px">On Time</div><div style="font-size:8.5px;color:var(--ink-soft)">Gurantee</div></div>
    <div><svg width="40" height="36" viewBox="0 0 40 36" fill="none" stroke="#333" stroke-width="1.4"><rect x="8" y="6" width="18" height="26"/><rect x="16" y="2" width="18" height="22"/><circle cx="25" cy="12" r="4" stroke="var(--teal)"/></svg><div style="font-size:15px;font-weight:500;margin-top:6px">Fixed</div><div style="font-size:8.5px;color:var(--ink-soft)">All Inclusive Pricing</div></div>
    <div><svg width="40" height="36" viewBox="0 0 40 36" fill="none" stroke="#333" stroke-width="1.6"><text x="2" y="22" font-family="Ubuntu,sans-serif" font-size="14" font-weight="700" fill="#333" stroke="none">360</text><circle cx="35" cy="6" r="2.5" stroke="var(--teal)"/><path d="M4 28c8 5 24 5 30-4" stroke="var(--teal)"/></svg><div style="font-size:15px;font-weight:500;margin-top:6px">360</div><div style="font-size:8.5px;color:var(--ink-soft)">Degree Feedback</div></div>
    <div><svg width="40" height="36" viewBox="0 0 40 36" fill="none" stroke="#333" stroke-width="1.4"><rect x="4" y="12" width="16" height="22"/><rect x="14" y="2" width="8" height="8"/><rect x="24" y="14" width="10" height="14" stroke="var(--teal)"/></svg><div style="font-size:15px;font-weight:500;margin-top:6px">Preffered</div><div style="font-size:8.5px;color:var(--ink-soft)">Driver by Traveller</div></div>
    <div><svg width="40" height="36" viewBox="0 0 40 36" fill="none" stroke="#333" stroke-width="1.4"><rect x="4" y="4" width="24" height="28"/><path d="M8 10h16M8 16h4M14 16h4M20 16h4M8 22h4M14 22h4" stroke="var(--teal)"/><rect x="30" y="8" width="6" height="24"/></svg><div style="font-size:15px;font-weight:500;margin-top:6px">Account</div><div style="font-size:8.5px;color:var(--ink-soft)">Reporting</div></div>
  </div>
</section>

<!-- ========== ROW 6 ========== -->
<section class="slide" style="left:0;top:1050px;width:375px;height:210px">
  <div class="h-slide" style="top:14px;font-size:10px">KLV for Agents</div>
  <div class="sub" style="top:30px">Your Subtitle Goes Here</div>
  <div class="photo red" role="img" aria-label="Red car photograph" style="left:32px;top:56px;width:178px;height:133px"></div>
  <div class="photo cool" role="img" aria-label="Fuel station photograph" style="left:210px;top:56px;width:66px;height:66px"></div>
  <div class="photo grey" role="img" aria-label="Car mirror photograph" style="left:276px;top:56px;width:66px;height:66px"></div>
  <div class="abs" style="left:210px;top:122px;width:132px;height:67px;background:var(--teal);color:#fff;padding:10px 10px">
    <div style="font-size:7px;font-weight:500">The Journey Matters</div>
    <div style="font-size:3.6px;line-height:1.4;margin-top:4px">If you are a travel agent, arranging ground transport for your traveller is important. At KLV we partner with a range of businesses to provide professional, reliable and safe service.</div>
  </div>
  <div class="footer"><span>Ride Ready</span><span>Page Number 17</span></div>
</section>

<section class="slide" style="left:375px;top:1050px;width:375px;height:210px">
  <div class="h-slide" style="top:14px;font-size:10px">KLV for Business</div>
  <div class="sub" style="top:30px">Your Subtitle Goes Here</div>
  <div class="photo dark" role="img" aria-label="Passenger in car at night photograph" style="left:9px;top:50px;width:90px;height:89px"></div>
  <div class="abs" style="left:99px;top:50px;width:90px;height:45px;background:var(--teal);color:#fff;padding:9px 6px">
    <div style="font-size:4.5px"><b>HIGH</b> Quality Transfer</div><div style="font-size:3.5px;margin-top:2px;line-height:1.4">Lorem ipsum dolor sit amet, consectetur adipiscing elit</div>
  </div>
  <div class="photo dusk" role="img" aria-label="City street photograph" style="left:99px;top:95px;width:90px;height:90px"></div>
  <div class="abs" style="left:9px;top:139px;width:90px;height:46px;background:#3a3a3a;color:#fff;padding:10px 5px">
    <div style="font-size:4.5px"><b>RELIABLE</b> On Time</div><div style="font-size:3.5px;margin-top:2px;line-height:1.4">Lorem ipsum dolor sit amet, consectetur adipiscing elit</div>
  </div>
  <div class="photo cool" role="img" aria-label="Businessman walking photograph" style="left:189px;top:50px;width:90px;height:135px"></div>
  <div class="photo light" role="img" aria-label="Woman with tablet photograph" style="left:283px;top:50px;width:82px;height:67px"></div>
  <div class="photo grey" role="img" aria-label="Man on phone photograph" style="left:283px;top:119px;width:82px;height:66px"></div>
  <div class="footer"><span>Ride Ready</span><span>Page Number 18</span></div>
</section>

<!-- ========== ROW 7 ========== -->
<section class="slide" style="left:0;top:1260px;width:375px;height:210px">
  <div class="h-slide" style="top:14px;font-size:10px">KLV for Drivers</div>
  <div class="sub" style="top:30px">Your Subtitle Goes Here</div>
  <div class="photo grey" role="img" aria-label="Hands on steering wheel photograph" style="left:48px;top:50px;width:93px;height:135px"></div>
  <div class="abs" style="left:48px;top:145px;width:93px;height:40px;background:#3a3a3a;color:#fff;padding:7px 8px"><div style="font-size:4.5px;font-weight:500">Lorem ipsum</div><div style="font-size:3.5px;line-height:1.4">Lorem ipsum dolor sit amet, consectetur adipiscing elit, sed do eiusmod</div></div>
  <div class="abs" style="left:141px;top:50px;width:93px;height:46px;background:var(--teal);color:#fff;padding:6px 8px"><div style="font-size:4.5px;font-weight:500">Lorem ipsum</div><div style="font-size:3.5px;line-height:1.4">Lorem ipsum dolor sit amet, consectetur adipiscing elit, sed do eiusmod</div></div>
  <div class="photo warm" role="img" aria-label="Driver at wheel photograph" style="left:141px;top:96px;width:93px;height:89px"></div>
  <div class="photo dark" role="img" aria-label="Man handing over car key photograph" style="left:234px;top:50px;width:93px;height:135px"></div>
  <div class="footer"><span>Ride Ready</span><span>Page Number 19</span></div>
</section>

<section class="slide" style="left:375px;top:1260px;width:375px;height:210px">
  <div class="h-slide" style="top:14px;font-size:10px">KLV for Business</div>
  <div class="sub" style="top:30px">Your Subtitle Goes Here</div>
  <div class="abs" style="left:25px;top:50px;width:323px;display:grid;grid-template-columns:repeat(3,1fr);gap:12px">
    <div><div class="photo cool" role="img" aria-label="Airport seating photograph" style="position:relative;height:62px"></div><div style="background:var(--teal);color:#fff;height:78px;padding:8px 10px"><div style="font-size:6px;font-weight:500">Lorem Ipsum</div><div style="font-size:3.5px">Dolor sit amet</div><div style="font-size:3.6px;line-height:1.4;margin-top:5px">Lorem ipsum dolor sit amet, consectetur adipiscing elit, sed do eiusmod</div><div style="margin-top:8px"><span class="btn round">Read More</span></div></div></div>
    <div><div class="photo warm" role="img" aria-label="Traveller in terminal photograph" style="position:relative;height:62px"></div><div style="background:#3a3a3a;color:#fff;height:78px;padding:8px 10px"><div style="font-size:6px;font-weight:500">Dolor Sit Amet</div><div style="font-size:3.5px">Dolor sit amet</div><div style="font-size:3.6px;line-height:1.4;margin-top:5px">Lorem ipsum dolor sit amet, consectetur adipiscing elit, sed do eiusmod</div><div style="margin-top:8px"><span class="btn round" style="background:var(--teal)">Read More</span></div></div></div>
    <div><div class="photo dark" role="img" aria-label="Hand with phone photograph" style="position:relative;height:62px"></div><div style="background:var(--teal);color:#fff;height:78px;padding:8px 10px"><div style="font-size:6px;font-weight:500">Consectetur</div><div style="font-size:3.5px">Dolor sit amet</div><div style="font-size:3.6px;line-height:1.4;margin-top:5px">Lorem ipsum dolor sit amet, consectetur adipiscing elit, sed do eiusmod</div><div style="margin-top:8px"><span class="btn round">Read More</span></div></div></div>
  </div>
  <div class="footer"><span>Ride Ready</span><span>Page Number 20</span></div>
</section>

<section class="slide" style="left:750px;top:1260px;width:375px;height:210px">
  <div class="photo grey" role="img" aria-label="Silver car in motion photograph" style="left:0;top:0;width:375px;height:105px"></div>
  <div class="abs" style="left:25px;top:115px;width:330px;display:grid;grid-template-columns:repeat(4,1fr);gap:6px">
    <div><svg class="ico" viewBox="0 0 26 26"><circle cx="13" cy="9" r="5"/><path class="tl" d="M5 24c1-6 15-6 16 0"/></svg><div style="font-size:5.5px;font-weight:500;margin-top:2px">KLV for Business</div><div class="tiny" style="font-size:3.6px">Lorem ipsum dolor sit amet, consectetur adipiscing elit, sed do eiusmod</div><div style="margin-top:4px"><span class="btn">Know More</span></div></div>
    <div><svg class="ico" viewBox="0 0 26 26"><rect x="4" y="6" width="18" height="16"/><path class="tl" d="M4 11h18M9 4v4M17 4v4"/></svg><div style="font-size:5.5px;font-weight:500;margin-top:2px">KLV for Events</div><div class="tiny" style="font-size:3.6px">Lorem ipsum dolor sit amet, consectetur adipiscing elit, sed do eiusmod</div><div style="margin-top:4px"><span class="btn">Know More</span></div></div>
    <div><svg class="ico" viewBox="0 0 26 26"><circle cx="13" cy="9" r="5"/><path class="tl" d="M5 24c1-6 15-6 16 0"/><path d="M9 4h8"/></svg><div style="font-size:5.5px;font-weight:500;margin-top:2px">KLV for Agents</div><div class="tiny" style="font-size:3.6px">Lorem ipsum dolor sit amet, consectetur adipiscing elit, sed do eiusmod</div><div style="margin-top:4px"><span class="btn">Know More</span></div></div>
    <div><svg class="ico" viewBox="0 0 26 26"><circle cx="13" cy="10" r="5"/><path class="tl" d="M7 24c1-5 11-5 12 0"/><path d="M9 4h8l-1 2h-6z"/></svg><div style="font-size:5.5px;font-weight:500;margin-top:2px">KLV for Drivers</div><div class="tiny" style="font-size:3.6px">Lorem ipsum dolor sit amet, consectetur adipiscing elit, sed do eiusmod</div><div style="margin-top:4px"><span class="btn">Know More</span></div></div>
  </div>
</section>

<section class="slide" style="left:1125px;top:1260px;width:375px;height:210px;background:#2b2d33">
  <div class="photo dark" role="img" aria-label="Dark road photograph" style="inset:0;background:linear-gradient(160deg,#3d4048,#24262b 60%,#1d1e22)"></div>
  <div class="h-slide" style="top:22px;color:#fff;font-size:18px;font-weight:500">Friendly</div>
  <div class="h-slide" style="top:45px;color:#ddd;font-size:10px;font-weight:300">And Professional Drivers</div>
  <div class="abs" style="left:110px;top:67px;width:155px;text-align:center;font-size:4px;color:#ccc;line-height:1.4">Lorem ipsum dolor sit amet, consectetur adipiscing elit, sed do eiusmod tempor incididunt ut labore et dolore magna aliqua. Duis aute irure dolor in reprehenderit.</div>
  <div class="abs" style="left:20px;top:103px;width:335px;display:grid;grid-template-columns:repeat(3,1fr);text-align:center;color:#ccc;font-size:3.8px;line-height:1.4">
    <div><svg width="30" height="30" viewBox="0 0 30 30" fill="none" stroke="#fff" stroke-width="1.4"><circle cx="15" cy="15" r="12"/><circle cx="15" cy="15" r="7"/><circle cx="15" cy="15" r="2" fill="#fff"/></svg><div style="padding:0 20px;margin-top:8px">Lorem ipsum dolor sit amet, consectetur adipiscing elit, sed do eiusmod tempor incididunt ut labore et dolore</div></div>
    <div><svg width="30" height="30" viewBox="0 0 30 30" fill="none" stroke="#fff" stroke-width="1.6"><path d="M3 14l6-6 6 4 6-4 6 6-10 9z"/></svg><div style="padding:0 20px;margin-top:8px">Lorem ipsum dolor sit amet, consectetur adipiscing elit, sed do eiusmod tempor incididunt ut labore et dolore</div></div>
    <div><svg width="30" height="30" viewBox="0 0 30 30" fill="none" stroke="#fff" stroke-width="1.4"><rect x="7" y="3" width="16" height="24"/><path d="M10 10h10M10 15h10M10 20h10"/></svg><div style="padding:0 20px;margin-top:8px">Lorem ipsum dolor sit amet, consectetur adipiscing elit, sed do eiusmod tempor incididunt ut labore et dolore</div></div>
  </div>
</section>

</div>
</body>
</html>
```